Business Card Design

Bramwell Pantry is the name of my health coaching business. My tag line is "Wellness Made for Everyday Living." I will be working with clients one-on-one and in groups. My target clients are women "of a certain age" who want to be more comfortable in their own skin. We will work together in a 6-month program. The coaching sessions will take place in my kitchen. I will also be conducting monthly cooking classes and field trips - to farmer's markets, speciality markets etc.. for my clients.
Updates

the business name is Bramwell Pantry - I'm not sure how the p got in there at the end of the name

Thank you

Please include the website - www.bramwellpantry-example.com and the tag line:

Where good health meets real life on the business card.

Thank you

Please add the phone number to the business card - sorry, I forgot to state that in the original brief

(555) 218-4476

Target Market(s)

Women "of a certain age" who want to be more comfortable in their own skin

Industry/Entity Type

Cooking

Contact Information for Business Card

Bramwell Pantry
Where good health meets real life

Harriet Dunmore
Health Coach
(555) 218-4476

Font styles to use
Serif
Sans Serif

Requirements
Must have
• front & back design
I typical like soft colors - and have tended toward greens over time - I'm open although I would not like bright reds, yellows etc..

```html
<!DOCTYPE html>
<html lang="en">
<head>
<meta charset="utf-8">
<title>Bramwell Pantry – Business Card</title>
<link rel="stylesheet" href="https://fonts.googleapis.com/css2?family=Tinos:wght@400;700&family=Questrial&display=swap">
<style>
  :root {
    --card-bg: #ffffff;
    --accent-green: #8ee51c;
    --rule-grey: #7a7f7c;
    --text-dark: #333333;
    --text-web: #444444;
  }
  * { margin: 0; padding: 0; box-sizing: border-box; }
  html, body {
    width: 1200px;
    height: 687px;
    overflow: hidden;
    background: var(--card-bg);
  }
  .card {
    position: relative;
    width: 1200px;
    height: 687px;
    background: var(--card-bg);
    font-family: "Tinos", "Times New Roman", serif;
    color: var(--text-dark);
  }
  .rule-vertical {
    position: absolute;
    left: 785px;
    top: 0;
    width: 7px;
    height: 687px;
    background: var(--accent-green);
  }
  .rule-horizontal {
    position: absolute;
    left: 0;
    top: 601px;
    width: 1200px;
    height: 7px;
    background: var(--rule-grey);
  }
  .brand-name {
    position: absolute;
    left: 140px;
    top: 262px;
    font-family: "Tinos", "Times New Roman", serif;
    font-size: 66px;
    font-weight: 400;
    line-height: 1;
    color: var(--rule-grey);
    letter-spacing: 1px;
    white-space: nowrap;
  }
  .brand-tagline {
    position: absolute;
    left: 303px;
    top: 364px;
    font-family: "Questrial", "Century Gothic", sans-serif;
    font-size: 19px;
    line-height: 1;
    color: var(--text-dark);
    white-space: nowrap;
  }
  .person {
    position: absolute;
    right: 46px;
    top: 156px;
    text-align: right;
  }
  .person-name {
    font-size: 34px;
    line-height: 1.1;
  }
  .person-title {
    font-size: 22px;
    line-height: 1.3;
  }
  .contact {
    position: absolute;
    right: 46px;
    top: 383px;
    text-align: right;
    font-size: 22px;
    line-height: 36px;
    list-style: none;
  }
  .contact .email { line-height: 32px; }
  .website {
    position: absolute;
    left: 140px;
    top: 640px;
    font-size: 24px;
    font-weight: 700;
    letter-spacing: 1.5px;
    color: var(--text-web);
    white-space: nowrap;
  }
</style>
</head>
<body>
  <div class="card">
    <div class="rule-horizontal"></div>
    <div class="rule-vertical"></div>

    <div class="brand-name">Bramwell Pantry</div>
    <div class="brand-tagline">Wellness Made for Everyday Living.</div>

    <div class="person">
      <div class="person-name">Harriet Dunmore</div>
      <div class="person-title">Health Coach</div>
    </div>

    <ul class="contact">
      <li>123 Alphabet St.</li>
      <li>City, State Zip</li>
      <li>(555) 218-4476</li>
      <li class="email">email@address.com</li>
    </ul>

    <div class="website">WWW.BRAMWELLPANTRY-EXAMPLE.COM</div>
  </div>
</body>
</html>
```